Crestline Slate & Tile Needs a Business Card

Attached you will find your logo, my photo and design guidelines for a new business card. The final design will need two separate files to create an embossed card. The cards will be printed by www.plinkprint.com (Instructions below)
Format is the Zib SQUARE card
Crestline Slate And Tile is a brick and mortar, retail stone and tile shop.
One the front:
Crestline Slate And Tile
Gerald Finchcombe
Owner
48207 Vesper Hollow Blvd
Suite R & T
Charlotte, NC 28953
Cell: 704-555-0183
Web: www.CrestlineSlateAndTile.com
(Make each word of the domain a different or alternating color)
On the back;
Something that shows beautiful colorful tile
Follow the design guide closely please. For more information see this page that describes creating the spot gloss file: https://www.plinkprint.com/us/business-cards/design-guidelines-spot-gloss
The logo is what we would like to have raised spot glossed.
Format is the Zib SQUARE card. See attahced guidlines.

```html
<!DOCTYPE html>
<html lang="en">
<head>
<meta charset="utf-8">
<title>Crestline Slate &amp; Tile — Square Business Card</title>
<link href="https://fonts.googleapis.com/css2?family=Montserrat:wght@400;500;600;800&display=swap" rel="stylesheet">
<style>
  :root {
    --backdrop-top: #c9c9c9;
    --backdrop-bottom: #a3a3a3;
    --card-white: #ffffff;
    --ink-navy: #1f2a38;
    --ink-body: #222222;
    --copper: #c47a45;
    --gold: #b8924a;
    --rose: #d8a3a3;
    --tile-navy: #24384f;
    --tile-terracotta: #b5552f;
    --tile-ochre: #d4a544;
    --tile-sage: #7d9476;
    --tile-cream: #e9dcc4;
  }
  * { box-sizing: border-box; margin: 0; padding: 0; }
  html, body {
    width: 1200px; height: 815px; overflow: hidden;
  }
  body {
    background: linear-gradient(180deg, var(--backdrop-top), var(--backdrop-bottom));
    font-family: "Montserrat", Arial, sans-serif;
    position: relative;
  }
  .card {
    position: absolute;
    top: 172px;
    width: 470px; height: 470px;
    background: var(--card-white);
    box-shadow: 0 6px 18px rgba(0,0,0,0.25);
  }
  .card--front { left: 90px; }
  .card--back { left: 640px; }
  .card__frame {
    position: absolute; inset: 20px;
    border: 1.5px solid var(--copper);
  }
  .front__content {
    position: absolute; inset: 20px;
    display: flex; flex-direction: column; align-items: center;
    padding-top: 56px;
    text-align: center;
  }
  .brand {
    display: flex; align-items: center; gap: 14px;
  }
  .brand__mark {
    width: 34px; height: 34px;
    background: var(--copper);
  }
  .brand__name {
    font-weight: 500;
    font-size: 20px;
    letter-spacing: 3px;
    color: var(--ink-navy);
    text-transform: uppercase;
  }
  .person__name {
    margin-top: 36px;
    font-weight: 800;
    font-size: 25px;
    letter-spacing: 0.5px;
    color: var(--ink-navy);
    text-transform: uppercase;
  }
  .person__role {
    margin-top: 2px;
    font-weight: 500;
    font-size: 12px;
    letter-spacing: 1px;
    color: var(--ink-navy);
  }
  .person__rule {
    margin-top: 10px;
    width: 22px; height: 1.5px;
    background: var(--rose);
  }
  .divider {
    margin-top: 16px;
    display: flex; align-items: center; gap: 8px;
  }
  .divider__line {
    width: 70px; height: 1px;
    background: var(--gold);
  }
  .divider__icons { display: flex; gap: 4px; }
  .icon {
    width: 18px; height: 18px;
  }
  .contact {
    margin-top: 8px;
    font-size: 14px;
    line-height: 1.4;
    color: var(--ink-body);
  }
  .contact__word--a { color: var(--ink-navy); font-weight: 600; }
  .contact__word--b { color: var(--copper); font-weight: 600; }
  .address {
    margin-top: 8px;
    font-size: 14px;
    line-height: 1.4;
    color: var(--ink-body);
  }
  .tile-feature {
    position: absolute; inset: 22px;
    background:
      radial-gradient(circle at 50% 50%, var(--tile-cream) 0%, transparent 22%),
      radial-gradient(circle at 20% 25%, var(--tile-terracotta) 0%, transparent 45%),
      radial-gradient(circle at 80% 25%, var(--tile-ochre) 0%, transparent 45%),
      radial-gradient(circle at 20% 78%, var(--tile-sage) 0%, transparent 45%),
      radial-gradient(circle at 80% 78%, var(--tile-terracotta) 0%, transparent 42%),
      var(--tile-navy);
  }
</style>
</head>
<body>

  <section class="card card--front" aria-label="Business card front">
    <div class="card__frame"></div>
    <div class="front__content">
      <div class="brand">
        <div class="brand__mark"></div>
        <div class="brand__name">Crestline Slate &amp; Tile</div>
      </div>

      <div class="person__name">Gerald Finchcombe</div>
      <div class="person__role">OWNER</div>
      <div class="person__rule"></div>

      <div class="divider">
        <span class="divider__line"></span>
        <span class="divider__icons">
          <svg class="icon" viewBox="0 0 18 18" aria-hidden="true">
            <circle cx="9" cy="9" r="9" fill="var(--gold)"/>
            <path d="M6 5 L7.6 5 L8.3 7 L7.3 7.8 Q8 9.6 10.2 10.7 L11 9.7 L13 10.4 L13 12 Q12.5 13 11 12.8 Q6.5 11.8 5.2 7 Q5 5.5 6 5 Z" fill="#fff"/>
          </svg>
          <svg class="icon" viewBox="0 0 18 18" aria-hidden="true">
            <circle cx="9" cy="9" r="9" fill="var(--gold)"/>
            <circle cx="9" cy="9" r="4.5" fill="none" stroke="#fff" stroke-width="1.1"/>
            <ellipse cx="9" cy="9" rx="2" ry="4.5" fill="none" stroke="#fff" stroke-width="0.9"/>
            <line x1="4.5" y1="9" x2="13.5" y2="9" stroke="#fff" stroke-width="0.9"/>
          </svg>
        </span>
        <span class="divider__line"></span>
      </div>

      <div class="contact">
        <div>Cell: 704-555-0183</div>
        <div>Web: www.<span class="contact__word--a">Crestline</span><span class="contact__word--b">Slate</span><span class="contact__word--a">And</span><span class="contact__word--b">Tile</span>.com</div>
      </div>

      <div class="divider">
        <span class="divider__line"></span>
        <svg class="icon" viewBox="0 0 18 18" aria-hidden="true">
          <circle cx="9" cy="9" r="9" fill="var(--gold)"/>
          <path d="M9 4 Q12.2 4 12.2 7.2 Q12.2 9.5 9 13.5 Q5.8 9.5 5.8 7.2 Q5.8 4 9 4 Z" fill="#fff"/>
          <circle cx="9" cy="7.2" r="1.3" fill="var(--gold)"/>
        </svg>
        <span class="divider__line"></span>
      </div>

      <div class="address">
        <div>48207 Vesper Hollow Blvd</div>
        <div>Suite R &amp; T</div>
        <div>Charlotte, NC 28953</div>
      </div>
    </div>
  </section>

  <section class="card card--back" aria-label="Business card back">
    <div class="tile-feature" role="img" aria-label="Photograph of colourful patterned tile in navy, terracotta, ochre, sage and cream"></div>
    <div class="card__frame"></div>
  </section>

</body>
</html>
```